Kovalen Spinal Care and Performance

We need new business cards, something more modern, clean. On the back of the card maybe a quote. The Dr. likes, “The doctor of the future will give no medicine, but will interest his patient in the care of the human frame, in diet and in the cause and prevention of disease.” - Walter Brisby. We are open to other suggestions. We are a chiropractic office.

```html
<!DOCTYPE html>
<html lang="en">
<head>
<meta charset="utf-8">
<title>Kovalen Spinal Care and Performance – Business Cards</title>
<link href="https://fonts.googleapis.com/css2?family=Arimo:wght@400&family=Marcellus+SC&family=Pinyon+Script&display=swap" rel="stylesheet">
<style>
  :root {
    --stage: #2e2e30;
    --card: #ffffff;
    --purple: #6a2f7e;
    --purple-light: #7e3d92;
    --purple-deep: #2a1230;
    --green: #a6c02c;
    --green-deep: #4d671c;
    --ink-grey: #4a4a4a;
    --soft-grey: #6b6b6b;
    --white: #ffffff;
  }
  * { margin: 0; padding: 0; box-sizing: border-box; }
  html, body { width: 1200px; height: 880px; overflow: hidden; }
  body {
    background: var(--stage);
    display: flex;
    align-items: center;
    justify-content: center;
    gap: 40px;
    font-family: "Arimo", Arial, sans-serif;
  }
  .card {
    position: relative;
    width: 540px;
    height: 309px;
    background: var(--card);
    border-radius: 16px;
    overflow: hidden;
  }
  /* Back: quote */
  .card-back {
    display: flex;
    flex-direction: column;
    align-items: center;
    justify-content: center;
    text-align: center;
    padding: 0 40px;
  }
  .quote {
    font-size: 13.5px;
    line-height: 1.35;
    color: var(--ink-grey);
  }
  .quote-author {
    margin-top: 4px;
    font-family: "Pinyon Script", cursive;
    font-size: 18px;
    color: var(--soft-grey);
  }
  /* Front */
  .front-waves { position: absolute; inset: 0; width: 100%; height: 100%; }
  .practitioner {
    position: absolute;
    top: 22px;
    right: 28px;
    text-align: right;
    line-height: 1.2;
  }
  .practitioner-name {
    font-family: "Marcellus SC", serif;
    font-size: 20px;
    color: var(--purple);
    letter-spacing: 0.5px;
  }
  .practitioner-role {
    font-size: 12px;
    color: var(--ink-grey);
  }
  .practice-name {
    position: absolute;
    left: 34px;
    top: 110px;
    width: 240px;
    font-family: "Marcellus SC", serif;
    font-size: 22px;
    line-height: 1.2;
    color: var(--purple);
  }
  .contact {
    position: absolute;
    right: 22px;
    top: 172px;
    list-style: none;
    text-align: right;
    color: var(--white);
    font-size: 12px;
    line-height: 1.35;
  }
  .contact li { display: flex; align-items: center; justify-content: flex-end; gap: 6px; }
  .contact .address { display: block; margin-bottom: 6px; }
  .contact-icon { width: 15px; height: 15px; flex: none; }
</style>
</head>
<body>

  <section class="card card-back" aria-label="Card back">
    <p class="quote">“The doctor of the future will give no medicine,<br>
      but will interest his patient in the care<br>
      of the human frame, in diet and in the cause and prevention of disease.”</p>
    <p class="quote-author">- Walter Brisby -</p>
  </section>

  <section class="card card-front" aria-label="Card front">
    <svg class="front-waves" viewBox="0 0 540 309" aria-hidden="true">
      <defs>
        <linearGradient id="purpleFill" x1="1" y1="0" x2="0" y2="1">
          <stop offset="0" stop-color="var(--purple-light)"/>
          <stop offset="0.55" stop-color="var(--purple)"/>
          <stop offset="1" stop-color="var(--purple-deep)"/>
        </linearGradient>
        <linearGradient id="greenFill" x1="1" y1="0" x2="0" y2="1">
          <stop offset="0" stop-color="var(--green)"/>
          <stop offset="1" stop-color="var(--green-deep)"/>
        </linearGradient>
      </defs>
      <path class="wave-green" d="M0 268 C110 256 225 238 268 186 C248 250 160 285 0 294 Z" fill="url(#greenFill)"/>
      <path class="wave-dark" d="M540 78 C420 80 335 100 295 170 C262 238 200 294 60 309 L540 309 Z" fill="var(--purple-deep)"/>
      <path class="wave-purple" d="M540 94 C430 96 360 110 320 175 C285 240 230 296 130 309 L540 309 Z" fill="url(#purpleFill)"/>
      <path class="wave-highlight" d="M540 86 C425 88 348 104 308 172 C274 239 215 295 95 309" fill="none" stroke="var(--white)" stroke-width="3"/>
    </svg>

    <div class="practitioner">
      <p class="practitioner-name">Dr. Walter Brisby</p>
      <p class="practitioner-role">Owner</p>
    </div>

    <p class="practice-name">Kovalen Spinal Care and Performance</p>

    <ul class="contact">
      <li class="address">412 W Alder Ridge Rd, Suite B<br>Maplewood, Illinois 60199</li>
      <li>(555) 014-2290
        <svg class="contact-icon" viewBox="0 0 16 16" aria-hidden="true">
          <circle cx="8" cy="8" r="7" fill="none" stroke="var(--white)" stroke-width="1.3"/>
          <path d="M5.5 4.5 L7 4.3 L7.6 6.3 L6.7 7 C7.2 8.2 7.9 8.9 9 9.4 L9.7 8.5 L11.6 9.1 L11.4 10.6 C8 10.8 5 8 5.5 4.5 Z" fill="var(--white)"/>
        </svg>
      </li>
      <li>www.kovalenspinalcare.com
        <svg class="contact-icon" viewBox="0 0 16 16" aria-hidden="true">
          <circle cx="8" cy="8" r="7" fill="none" stroke="var(--white)" stroke-width="1.3"/>
          <circle cx="8" cy="8" r="4" fill="none" stroke="var(--white)" stroke-width="1"/>
          <path d="M4 8 H12 M8 4 V12" stroke="var(--white)" stroke-width="1"/>
        </svg>
      </li>
    </ul>
  </section>

</body>
</html>
```